Young, dynamic furniture company needs a new business card design

We require a new business card design for our modern furniture company which supplies furniture and appliances to the property and development market.
Quarrow Furnishing has become one of the leading furniture & appliance suppliers to the property market withing London. With over 10 years experience, we have increased our business to supply not only private landlords and managing agents, but also property developers, housing associations and local councils.
We offer not only a complete range of furniture which includes beds, wardrobes, dining sets and sofas, but also a high quality, full delivery and assembly service to help you with all our furnishing needs.

Target Market(s)

Private landlords, estate agents, letting agents, property management companies

Industry/Entity Type

Business

Contact Information for Business Card

Name,
Title,
Address,
Mobile,
Telephone,
Fax, Website, email address

Font styles to use
Sans Serif

Colors
3176b5
0555a3
85abd2
cfdeed

Requirements
Must have
• All the above information for each of our staff, along with our logo

```html
<!DOCTYPE html>
<html lang="en">
<head>
<meta charset="utf-8">
<title>Quarrow Furnishing – Business Card</title>
<link href="https://fonts.googleapis.com/css2?family=Arimo:wght@400;700&display=swap" rel="stylesheet">
<style>
  :root {
    --backdrop: #2e2a28;
    --card: #141517;
    --card-edge: #1d1e21;
    --blue-deep: #0555a3;
    --blue: #3176b5;
    --blue-soft: #85abd2;
    --blue-pale: #cfdeed;
    --text-light: #e9ebee;
    --text-muted: #9ea3aa;
    --divider: #4a4d53;
  }
  * { box-sizing: border-box; margin: 0; padding: 0; }
  html, body {
    width: 1200px; height: 864px; overflow: hidden;
    background: var(--backdrop);
    font-family: "Arimo", Arial, sans-serif;
  }
  .canvas { position: relative; width: 1200px; height: 864px; }
  .card {
    position: absolute;
    width: 620px; height: 354px;
    background: var(--card);
    border: 1px solid var(--card-edge);
    border-radius: 4px;
    box-shadow: 0 14px 30px rgba(0,0,0,.45);
  }
  .card--front { left: 70px; top: 60px; }
  .card--back { left: 510px; top: 450px; }

  .brand { display: flex; flex-direction: column; align-items: center; }
  .brand__mark {
    width: 54px; height: 54px; background: var(--blue); margin-bottom: 16px;
  }
  .brand__name {
    color: var(--text-light); font-size: 23px; font-weight: 400;
    letter-spacing: .5px; text-transform: uppercase; white-space: nowrap;
  }
  .brand__tagline {
    color: var(--text-muted); font-size: 11px; letter-spacing: .6px;
    text-transform: uppercase; margin-top: 4px; white-space: nowrap;
  }

  .card--front .brand { position: absolute; left: 0; right: 0; top: 70px; }
  .front__pitch {
    position: absolute; left: 0; right: 0; top: 232px;
    text-align: center; color: var(--text-muted);
    font-size: 15px; line-height: 1.45;
  }

  .card--back .brand { position: absolute; left: 22px; width: 290px; top: 100px; }
  .back__divider {
    position: absolute; left: 330px; top: 50px; width: 1px; height: 254px;
    background: linear-gradient(to bottom, transparent, var(--divider) 25%, var(--divider) 75%, transparent);
  }
  .contact { position: absolute; left: 356px; top: 56px; right: 20px; }
  .contact__name {
    color: var(--blue); font-size: 20px; text-transform: uppercase; letter-spacing: .5px;
  }
  .contact__title {
    color: var(--blue); font-size: 15px; text-transform: uppercase; margin-bottom: 8px;
  }
  .contact__address { color: var(--text-light); font-size: 14px; line-height: 1.4; margin-bottom: 6px; }
  .contact__list { list-style: none; }
  .contact__item {
    display: flex; align-items: center; gap: 10px;
    color: var(--text-light); font-size: 14px; line-height: 22px; white-space: nowrap;
  }
  .contact__icon { width: 13px; height: 13px; flex: none; fill: var(--blue-deep); }
</style>
</head>
<body>
<main class="canvas">

  <section class="card card--front">
    <div class="brand">
      <div class="brand__mark"></div>
      <div class="brand__name">Quarrow Furnishing</div>
      <div class="brand__tagline">Trade Furniture Solutions</div>
    </div>
    <p class="front__pitch">High quality, full delivery &amp; assembly<br>service to help you with all our furnishing needs.</p>
  </section>

  <section class="card card--back">
    <div class="brand">
      <div class="brand__mark"></div>
      <div class="brand__name">Quarrow Furnishing</div>
      <div class="brand__tagline">Trade Furniture Solutions</div>
    </div>

    <div class="back__divider"></div>

    <div class="contact">
      <div class="contact__name">Marcus Hale</div>
      <div class="contact__title">President</div>
      <div class="contact__address">2761 Kestrel Avenue<br>Oakridge, NY 11420</div>
      <ul class="contact__list">
        <li class="contact__item">
          <svg class="contact__icon" viewBox="0 0 16 16"><path d="M3 1h3l1.5 4-2 1.3a9 9 0 0 0 4.2 4.2L11 8.5l4 1.5v3a2 2 0 0 1-2 2A13 13 0 0 1 1 3a2 2 0 0 1 2-2z"/></svg>
          555 0142 7316
        </li>
        <li class="contact__item">
          <svg class="contact__icon" viewBox="0 0 16 16"><path d="M4 0h8a1 1 0 0 1 1 1v14a1 1 0 0 1-1 1H4a1 1 0 0 1-1-1V1a1 1 0 0 1 1-1zm1 2v10h6V2zm3 11a1 1 0 1 0 0 2 1 1 0 0 0 0-2z"/></svg>
          555 0187 4429
        </li>
        <li class="contact__item">
          <svg class="contact__icon" viewBox="0 0 16 16"><path d="M4 0h7v5H4zM1 6h14v8H1zm2 2v2h4V8zm8 0v1h2V8zm0 2v1h2v-1z"/></svg>
          555 0163 9082
        </li>
        <li class="contact__item">
          <svg class="contact__icon" viewBox="0 0 16 16"><path d="M0 3h16v10H0zm1.5 1.5L8 9l6.5-4.5V4h-13z"/></svg>
          marcus@quarrow.example
        </li>
        <li class="contact__item">
          <svg class="contact__icon" viewBox="0 0 16 16"><circle cx="8" cy="8" r="8"/><circle cx="8" cy="8" r="3" fill="#141517"/></svg>
          www.quarrow.example
        </li>
      </ul>
    </div>
  </section>

</main>
</body>
</html>
```